Biz card for my counselling/social work practice

Biz card design for my counselling practice, focus on well-being, I am a social worker who also teaches meditation and workshops but my main focus for the card is my counselling practice. My website reveals a gentle flowing quality which I would life reflected in my card. This business card will be designed to share with other practitioners who are looking for support with their clients to take their healing to another level or well-being.

Target Market(s)

professionals seeking mental health counselling/men/women/ those seeking to improve their well-being through insight based counselling to optimize their lives and process trauma or limiting patterns

Industry/Entity Type

Counsellor

Contact Information for Business Card

Info on the card: perhaps text is aligned left?
Marla Finch, MSW, RSW
Counsellor
250.555.0142
info@marlafinch.ca
www.marlafinch.ca

Please use a modern font doesn’t need to be the one chosen below. Thank you

Font styles to use
Serif

Colors
3176b5
33a6d7
33b8a4
6b449b
abd037
d2a4cc
e55fa2

Requirements
Must have
• My business card details on front
• Backside
• Accelerated Resolution Therapy
• Cognitive Behavioral Therapy
• Mindfulness Informed Therapy
Nice to have
• I would like the card to be basic, (white or creme without too much bold colour) and with perhaps a stripe or band of vertical colour in blue or green (or a merge of colour) perhaps embossed or in a negative space. (this is one idea, but do not want the card to be too feminine or interest only women as i see men too so this is only an idea, but not 100 percent on this.
• I do not have a logo. I would prefer to heart from my website not to be used in the design as i am considering modifying this and re-branding.
Should not have
• too bold colours or bright yellow/blacks. i Like tones that are greens, blues.

```html
<!DOCTYPE html>
<html lang="en">
<head>
<meta charset="utf-8">
<title>Marla Finch, MSW, RSW — Business Card</title>
<link rel="stylesheet" href="https://fonts.googleapis.com/css2?family=Mulish:wght@300;400;600;700&display=swap">
<style>
  :root {
    --page-bg: #2a2a2a;
    --card-white: #ffffff;
    --sky-blue: #2fa3d8;
    --teal-mid: #6bb3a0;
    --leaf-green: #9cc84a;
    --ink: #2b2b2b;
    --icon-green: #8cc63f;
  }
  * { box-sizing: border-box; margin: 0; padding: 0; }
  html, body {
    width: 1200px;
    height: 1021px;
    overflow: hidden;
    background: var(--page-bg);
    font-family: "Mulish", "Helvetica Neue", Arial, sans-serif;
  }
  .canvas {
    position: relative;
    width: 1200px;
    height: 1021px;
  }
  .card {
    position: absolute;
    left: 220px;
    width: 760px;
    height: 434px;
    overflow: hidden;
  }
  /* Back side */
  .card-back {
    top: 51px;
    background: linear-gradient(180deg, var(--sky-blue) 0%, var(--teal-mid) 45%, var(--leaf-green) 100%);
    display: flex;
    align-items: center;
    justify-content: center;
  }
  .services {
    list-style: none;
    color: #ffffff;
    font-weight: 300;
    font-size: 25px;
    line-height: 1.45;
    letter-spacing: 1px;
    text-align: left;
  }
  /* Front side */
  .card-front {
    top: 535px;
    background: var(--card-white);
  }
  .identity {
    position: absolute;
    left: 58px;
    top: 62px;
  }
  .name {
    color: var(--sky-blue);
    font-weight: 700;
    font-size: 34px;
    letter-spacing: 0.5px;
    line-height: 1.1;
  }
  .role {
    color: var(--ink);
    font-weight: 400;
    font-size: 20px;
    letter-spacing: 0.5px;
    margin-top: 2px;
  }
  .contacts {
    position: absolute;
    left: 58px;
    top: 228px;
    list-style: none;
    color: var(--ink);
    font-size: 21px;
    letter-spacing: 0.6px;
    line-height: 1.4;
  }
  .contacts li {
    display: flex;
    align-items: center;
    gap: 10px;
  }
  .contacts svg {
    width: 17px;
    height: 17px;
    flex: none;
  }
  .colour-band {
    position: absolute;
    top: 0;
    left: 518px;
    width: 142px;
    height: 100%;
    background: linear-gradient(180deg, var(--sky-blue) 0%, var(--teal-mid) 50%, var(--leaf-green) 100%);
    display: flex;
    align-items: flex-end;
    justify-content: center;
    padding-bottom: 92px;
  }
  .band-name {
    color: #ffffff;
    font-weight: 600;
    font-size: 17px;
    letter-spacing: 1px;
    text-align: center;
  }
</style>
</head>
<body>
  <main class="canvas">
    <section class="card card-back" aria-label="Card back">
      <ul class="services">
        <li>Accelerated Resolution Therapy</li>
        <li>Cognitive Behavioral Therapy</li>
        <li>Mindfulness Informed Therapy</li>
      </ul>
    </section>

    <section class="card card-front" aria-label="Card front">
      <div class="identity">
        <h1 class="name">Marla Finch, MSW, RSW</h1>
        <p class="role">Counsellor</p>
      </div>

      <ul class="contacts">
        <li>
          <svg viewBox="0 0 24 24" aria-hidden="true"><path fill="var(--icon-green)" d="M6.6 10.8a15.1 15.1 0 0 0 6.6 6.6l2.2-2.2c.3-.3.7-.4 1-.2 1.1.4 2.3.6 3.6.6.6 0 1 .4 1 1V20c0 .6-.4 1-1 1A17 17 0 0 1 3 4c0-.6.4-1 1-1h3.5c.6 0 1 .4 1 1 0 1.3.2 2.5.6 3.6.1.3 0 .7-.2 1z"/></svg>
          <span>250.555.0142</span>
        </li>
        <li>
          <svg viewBox="0 0 24 24" aria-hidden="true"><rect x="2" y="5" width="20" height="14" fill="none" stroke="var(--icon-green)" stroke-width="2"/><path d="M2 5l10 8 10-8" fill="none" stroke="var(--icon-green)" stroke-width="2"/></svg>
          <span>info@marlafinch.ca</span>
        </li>
        <li>
          <svg viewBox="0 0 24 24" aria-hidden="true"><g fill="none" stroke="var(--icon-green)" stroke-width="2"><circle cx="12" cy="12" r="10"/><ellipse cx="12" cy="12" rx="4" ry="10"/><path d="M2 12h20M4 7h16M4 17h16"/></g></svg>
          <span>www.marlafinch.ca</span>
        </li>
      </ul>

      <div class="colour-band">
        <span class="band-name">Marla Finch</span>
      </div>
    </section>
  </main>
</body>
</html>
```